Fennick Executive Search - New Business Card Design Project

We are an executive search firm called Fennick Executive Search based in the UK. We require a custom design for a business card. We're looking to convey a professional service to executives for executive search recruitment services. In terms of colours, we like dark blues and grays (maybe even silver incorporated somewhere if we go for a foiled type of card) but we're open to your artistic flare. See our current logo in attachments. We are totally open on design so long as the design is slick and professional.
Updates

Thanks for all your contributions of various designs. I have to say the quality of work has been amazing which is going to make our job quite difficult in the coming days on making a decision. Thanks to you all that have taken the time to submit designs thus far. We'll keep on reviewing and try to narrow down our selection as soon as possible.

Target Market(s)

Executive Search

Industry/Entity Type

Recruitment

Contact Information for Business Card

Fennick Executive Search,
Exclusively Sourcing & Hiring Senior Leaders
Gordon Pellbury, Managing Director,
07823 906417
0117 486 7132
gordon@fennickexecutive.co.uk
fennickexecutive.co.uk
58 Lindmoor Court, Hatherley Road, Bristol, BS32 9QJ

Font styles to use
Sans Serif
Other font styles liked:
• Roboto (which is used in our logo)

Requirements
Must have
• Our logo (It has a subtle fade on it from #02071d at top to #333649 at bottom)
• The logo can be on one side or both sides
• Must be elegant and professional
• We have 2nd slogan CONSULT | INSPIRE | INNOVATE | DELIVER which can be incorporated into the card
Nice to have
• Use of blues and grey colours
• Compatible with similar styling to our website fennickexecutive.co.uk
Should not have
• Must not be overly brash
• Must not contain cartoon characters

```html
<!DOCTYPE html>
<html lang="en">
<head>
<meta charset="utf-8">
<title>Fennick Executive Search – Business Card</title>
<link href="https://fonts.googleapis.com/css2?family=Roboto:wght@300;400;500;700&family=Roboto+Mono:wght@400&display=swap" rel="stylesheet">
<style>
  :root {
    --navy-top: #02071d;
    --navy-bottom: #333649;
    --navy: #1c2140;
    --ink: #20243f;
    --text-grey: #4a4d5c;
    --strip-grey: #5a5b60;
    --paper: #ffffff;
    --backdrop: #e4e5e9;
    --tagline: #c9ccd8;
  }
  * { box-sizing: border-box; margin: 0; padding: 0; }
  html, body { width: 1200px; height: 900px; overflow: hidden; }
  body {
    background: var(--backdrop);
    font-family: "Roboto", Arial, sans-serif;
    position: relative;
  }
  .card {
    position: absolute;
    left: 300px;
    width: 600px;
    height: 343px;
    border-radius: 18px;
    overflow: hidden;
    box-shadow: 0 10px 28px rgba(0,0,0,0.18);
  }

  /* Back side */
  .card-back {
    top: 50px;
    background: linear-gradient(180deg, var(--navy-top) 0%, var(--navy-bottom) 100%);
    color: #fff;
  }
  .card-back .map-area {
    position: absolute;
    left: 110px; top: 40px;
    width: 380px; height: 190px;
    border-radius: 40px;
    background: radial-gradient(ellipse at center, rgba(120,128,170,0.22) 0%, rgba(120,128,170,0.06) 60%, rgba(120,128,170,0) 80%);
  }
  .card-back .brand {
    position: absolute;
    top: 150px; left: 0; right: 0;
    text-align: center;
    font-size: 32px;
    font-weight: 500;
    letter-spacing: 1px;
    color: #ffffff;
  }
  .card-back .slogan {
    position: absolute;
    top: 250px; left: 0; right: 0;
    text-align: center;
    font-family: "Roboto Mono", monospace;
    font-size: 14px;
    letter-spacing: 1px;
    color: var(--tagline);
  }

  /* Front side */
  .card-front {
    top: 470px;
    background: var(--paper);
  }
  .card-front .edge-tab {
    position: absolute;
    left: -10px; top: 38px;
    width: 22px; height: 42px;
    border-radius: 10px;
    background: var(--navy);
  }
  .card-front .bottom-strip {
    position: absolute;
    left: 0; bottom: 0;
    width: 100%; height: 16px;
  }
  .card-front .holder {
    position: absolute;
    left: 46px; top: 58px;
    color: var(--ink);
  }
  .holder .name { font-size: 19px; font-weight: 700; letter-spacing: 0.3px; }
  .holder .role { font-size: 14px; font-weight: 700; margin-top: 2px; }
  .contacts {
    position: absolute;
    left: 46px; top: 128px;
    list-style: none;
    color: var(--text-grey);
    font-size: 15px;
    font-weight: 400;
  }
  .contacts li {
    display: flex; align-items: center;
    height: 24px;
  }
  .contacts svg { width: 14px; height: 14px; margin-right: 12px; fill: none; stroke: var(--ink); stroke-width: 1.6; }
  .card-front .brand {
    position: absolute;
    right: 40px; top: 128px;
    color: var(--ink);
    font-size: 22px;
    font-weight: 700;
    letter-spacing: 0.6px;
    white-space: nowrap;
  }
  .card-front .rule {
    position: absolute;
    left: 250px; right: 40px; top: 166px;
    height: 2px;
    background: var(--ink);
  }
  .card-front .address {
    position: absolute;
    right: 40px; top: 236px;
    text-align: right;
    font-size: 16px;
    line-height: 1.35;
    color: var(--text-grey);
    font-style: normal;
  }
</style>
</head>
<body>

<section class="card card-back" aria-label="Business card back">
  <div class="map-area" role="img" aria-label="Faint dotted world map behind the company name"></div>
  <p class="brand">FENNICK EXECUTIVE SEARCH</p>
  <p class="slogan">Exclusively Sourcing &amp; Hiring Senior Leaders</p>
</section>

<section class="card card-front" aria-label="Business card front">
  <div class="edge-tab"></div>

  <div class="holder">
    <p class="name">GORDON PELLBURY</p>
    <p class="role">Managing Director</p>
  </div>

  <ul class="contacts">
    <li>
      <svg viewBox="0 0 14 14"><path d="M3 1.5 L5 1.5 L6 4.5 L4.5 5.5 C5.3 7.3 6.7 8.7 8.5 9.5 L9.5 8 L12.5 9 L12.5 11 C12.5 12 11.5 12.7 10.5 12.5 C6 11.5 2.5 8 1.5 3.5 C1.3 2.5 2 1.5 3 1.5 Z"/></svg>
      07823 906417
    </li>
    <li>
      <svg viewBox="0 0 14 14"><rect x="3.5" y="1" width="7" height="12" rx="1.2"/><line x1="6" y1="11" x2="8" y2="11"/></svg>
      0117 486 7132
    </li>
    <li>
      <svg viewBox="0 0 14 14"><rect x="1" y="3" width="12" height="8.5" rx="0.8"/><polyline points="1,3.5 7,8 13,3.5"/></svg>
      gordon@fennickexecutive.co.uk
    </li>
    <li>
      <svg viewBox="0 0 14 14"><circle cx="7" cy="7" r="5.8"/><ellipse cx="7" cy="7" rx="2.5" ry="5.8"/><line x1="1.2" y1="7" x2="12.8" y2="7"/></svg>
      fennickexecutive.co.uk
    </li>
  </ul>

  <p class="brand">FENNICK EXECUTIVE SEARCH</p>

  <div class="rule"></div>

  <address class="address">58 Lindmoor Court, Hatherley Road,<br>Bristol, BS32 9QJ</address>

  <svg class="bottom-strip" viewBox="0 0 600 16" preserveAspectRatio="none" aria-hidden="true">
    <polygon points="0,0 372,0 360,16 0,16" fill="#1c2140"/>
    <polygon points="380,0 600,0 600,16 368,16" fill="#5a5b60"/>
  </svg>
</section>

</body>
</html>
```